Counting Toward Purpose institute for nonprofits needs brochure

The Counting Toward Purpose performance management institute helps nonprofits clarify the intended impact of their programs on clients. What does a nonprofit want to accomplish - and what does it need to measure so that it can tell if they've achieved impact? The Institute is about to recruit participanting organizations. We have a lot of wording on a 2 page "flyer" that describes the institute...but it is a very ugly piece that looks unprofessional. We are looking for designs that are consistent with the KRT Advisory Group look (see our website). We are aware that we may have too much wording.

Target Market(s)

Nonprofit organization Executive Directors

Industry/Entity Type

Non-Profit

Font styles to use
Sans Serif

Requirements
Must have
• Must be able to be emailed to a client and printed on 8.5x11 paper. Doesn't matter to me if that makes it a tri-fold or two-fold.
• Need to be able to drop in later the actual dates of the program.
• Go to our website to see how we present ourselves. www.krtadvisoryhub.example
Nice to have
• See our website for KRT Advisory's "look". Our colors are green and gray (in the logo), with complementary colors of blue and orange.
• Looking for creativity in the graphics design. Our two page document has way too many words. The word impact is very important to the concept of performance management (and I'm not sure it's in the 2 page write up) - so you could do something with that word if you wanted to.
• Could use Davina's pic if it makes sense.
Should not have
• No new logo for the Counting Toward Purpose institute. It should be clear that KRT Advisory Group is the entity that offers the institute.

```html
<!DOCTYPE html>
<html lang="en">
<head>
<meta charset="utf-8">
<title>Counting Toward Purpose – KRT Advisory Group Institute Brochure</title>
<link rel="stylesheet" href="https://fonts.googleapis.com/css2?family=Mulish:wght@300;400;700;800&display=swap">
<style>
  :root{
    --page-bg:#ebe8e3;
    --paper:#ffffff;
    --ink:#5b5c5f;
    --green:#84bd3f;
    --grey-left:#77787b;
    --grey-right:#7f8084;
    --white:#ffffff;
  }
  *{box-sizing:border-box;margin:0;padding:0}
  html,body{width:1200px;height:1200px;overflow:hidden}
  body{
    background:var(--page-bg);
    font-family:"Mulish",Arial,sans-serif;
    position:relative;
  }
  .spread{
    position:absolute;left:80px;top:198px;width:1040px;height:802px;
    box-shadow:0 8px 22px rgba(0,0,0,.22);
  }
  .panel{position:absolute;top:0;width:520px;height:802px}
  .panel--inside{left:0}
  .panel--cover{left:520px}

  .panel__upper{position:absolute;left:0;top:0;width:520px;height:503px}
  .panel--inside .panel__upper{
    background:linear-gradient(90deg,var(--paper) 0%,var(--paper) 58%,#ededed 100%);
  }
  .photo-area{
    background:
      radial-gradient(ellipse at 62% 30%,rgba(226,196,176,.55) 0%,rgba(226,196,176,0) 35%),
      linear-gradient(110deg,#d9d9dc 0%,#c9c8cb 18%,#2b2b30 30%,#3a3a40 48%,#d7d3d0 62%,#2a2a2f 72%,#ecebea 86%,#f2f2f2 100%);
  }
  .green-band{
    position:absolute;left:0;top:503px;width:1040px;height:10px;background:var(--green);z-index:2;
  }
  .panel__lower{position:absolute;left:0;top:513px;width:520px;height:289px}
  .panel--inside .panel__lower{background:var(--grey-left)}
  .panel--cover .panel__lower{background:var(--grey-right)}

  .brand-mark{
    position:absolute;left:38px;top:34px;
    font-weight:300;font-size:33px;letter-spacing:-.5px;color:var(--ink);
  }
  .tagline-small{
    position:absolute;left:98px;top:92px;
    font-size:7px;letter-spacing:1.3px;line-height:13.6px;color:var(--ink);text-transform:uppercase;
  }
  .tagline-small span:last-child{font-weight:700}

  .body-copy{
    position:absolute;top:168px;width:213px;
    font-size:10.4px;line-height:13.05px;font-weight:300;color:var(--ink);
    text-align:justify;
  }
  .body-copy p{margin-bottom:13px}
  .body-copy--left{left:38px}
  .body-copy--right{left:269px}
  .body-copy strong{font-weight:700}

  .contact{
    position:absolute;left:0;top:115px;width:520px;text-align:center;
    color:var(--white);font-size:15.5px;line-height:19.4px;font-weight:300;
  }
  .cover-brand{
    position:absolute;left:0;top:82px;width:520px;text-align:center;
    font-weight:300;font-size:54px;letter-spacing:-1px;color:var(--white);
  }
  .cover-tagline{
    position:absolute;left:0;top:181px;width:520px;text-align:center;
    color:var(--white);font-weight:800;font-size:20.5px;line-height:25.6px;letter-spacing:.3px;
  }
</style>
</head>
<body>
  <div class="spread">
    <section class="panel panel--inside">
      <div class="panel__upper">
        <div class="brand-mark">krtadvisory</div>
        <div class="tagline-small"><span>Performance</span><br><span>Management</span><br><span>Institute</span></div>

        <div class="body-copy body-copy--left">
          <p>Counting Toward Purpose is a performance management institute offered by KRT Advisory Group. It helps nonprofits define the impact they intend to have on clients.</p>
          <p>Teams of executive directors, board members and program staff work through the core questions: What does your organization want to accomplish? What change should clients experience? What must you measure to know whether you have achieved impact?</p>
          <p>The Institute runs as a cohort. <strong>Program dates: to be announced.</strong> Each participating organization sends a team of two to four leaders, attends every session and completes brief assignments between meetings,</p>
        </div>

        <div class="body-copy body-copy--right">
          <p>with coaching from KRT Advisory partners. Our partners have worked with nonprofits as staff leaders, board members and funders. We have seen what works and what doesn't, how great programs need clear goals, and how impact looks different from different stakeholder sight lines.</p>
          <p><strong>Impact is the reason nonprofits exist.</strong> Measuring it helps you improve programs, tell your story to funders and show your board the difference your work makes. Participants leave with a logic model, a short set of outcome indicators and a data plan. The Institute is now recruiting participating organizations. Contact KRT Advisory Group to reserve a place for your team.</p>
        </div>
      </div>
      <div class="panel__lower">
        <div class="contact">
          2450 Alder Grove Lane, Fairview, MO 63199<br>
          78 Ridgecrest Court, Millbrook, NC 28799<br>
          555-014-7720 | info@krtadvisoryhub.example<br>
          www.krtadvisoryhub.example
        </div>
      </div>
    </section>

    <section class="panel panel--cover">
      <div class="panel__upper photo-area" role="img" aria-label="Photo of nonprofit leaders in business attire seated at a conference table, applauding"></div>
      <div class="panel__lower">
        <div class="cover-brand">krtadvisory</div>
        <div class="cover-tagline">COUNTING TOWARD PURPOSE<br>AN INSTITUTE FOR IMPACT</div>
      </div>
    </section>

    <div class="green-band"></div>
  </div>
</body>
</html>
```